Business Card Design Project

We are looking for a new business card design for a Drilling company in WA, Australia.

We are in between offices, however require a design in the meantime due to some upcoming events with our basic information.

The Logo for our company is Blue and Grey and would like this colour scheme throughout.

We are quite a new company so would like a memorable design that stands out and communicates a strong commitment to safety, quality of work and performance.

The company name is Ironbark Boring Group (IBG)

The details to be included are as follows:

Gavin Thorley
Managing Director
m.0481639207
e.gavin@ibgpty.com.au

Martin Thorley
Director
m.0419852637
e.martin@ibgpty.com.au

Industry/Entity Type

Events

Requirements
Must have
• Under the Logo, we would like 'Western Australia'

```html
<!DOCTYPE html>
<html lang="en">
<head>
<meta charset="utf-8">
<title>Ironbark Boring Group – Business Card</title>
<link rel="stylesheet" href="https://fonts.googleapis.com/css2?family=Open+Sans:wght@300;400;700;800&display=swap">
<style>
  :root {
    --navy-deep: #0d0a52;
    --navy: #13237a;
    --blue: #174a9a;
    --cyan: #1a86c0;
    --grey: #6e6e72;
    --grey-light: #9a9a9e;
    --white: #ffffff;
    --page: #e9eaee;
  }
  * { margin: 0; padding: 0; box-sizing: border-box; }
  html, body {
    width: 1200px; height: 1026px; overflow: hidden;
    background: var(--page);
    font-family: "Open Sans", Arial, sans-serif;
  }
  .sheet {
    position: relative; width: 1200px; height: 1026px;
    display: flex; flex-direction: column; align-items: center; justify-content: center;
    gap: 56px;
  }
  .card {
    position: relative; width: 700px; height: 428px;
    border-radius: 22px; overflow: hidden;
    box-shadow: 0 10px 28px rgba(10, 14, 50, 0.22);
  }

  /* Back side */
  .card--back {
    background: radial-gradient(ellipse at 70% 10%, #1a4f9e 0%, var(--navy) 55%, var(--navy-deep) 100%);
  }
  .card--back .brand {
    position: absolute; right: 40px; bottom: 38px; text-align: right; color: var(--white);
  }
  .brand__name {
    font-weight: 800; font-size: 34px; letter-spacing: 0.5px; line-height: 1; text-transform: uppercase;
  }
  .brand__region {
    margin-top: 10px; font-weight: 400; font-size: 14px; letter-spacing: 3px;
  }

  /* Front side */
  .card--front { background: var(--white); }
  .card--front .brand {
    position: absolute; left: 40px; top: 40px; color: var(--navy);
  }
  .card--front .brand__row { display: flex; align-items: center; gap: 12px; }
  .brand__mark { width: 22px; height: 22px; background: var(--navy); }
  .card--front .brand__region { color: var(--grey); margin-left: 34px; }

  .person {
    position: absolute; right: 44px; top: 196px; text-align: right;
  }
  .person__name { font-weight: 700; font-size: 28px; color: var(--navy); letter-spacing: 0.5px; }
  .person__role { font-weight: 300; font-size: 17px; color: var(--grey); margin-top: 2px; }

  .divider {
    position: absolute; left: 0; right: 0; top: 272px; height: 3px; background: var(--grey-light);
  }
  .band {
    position: absolute; left: 0; right: 0; top: 282px; bottom: 0;
    background: linear-gradient(90deg, var(--navy-deep) 0%, var(--navy) 45%, var(--blue) 75%, var(--cyan) 100%);
  }
  .contacts {
    position: absolute; right: 40px; top: 26px;
    display: flex; align-items: stretch; gap: 14px;
  }
  .contacts__text {
    text-align: right; color: var(--white); font-size: 17px; font-weight: 400; line-height: 30px;
  }
  .contacts__rule { width: 1px; background: rgba(255,255,255,0.7); }
  .contacts__icons { display: flex; flex-direction: column; justify-content: space-between; padding: 7px 0; }
  .contacts__icons svg { width: 16px; height: 16px; display: block; }
</style>
</head>
<body>
<main class="sheet">

  <section class="card card--back" aria-label="Card back">
    <div class="brand">
      <div class="brand__name">Ironbark Boring Group</div>
      <div class="brand__region">Western Australia</div>
    </div>
  </section>

  <section class="card card--front" aria-label="Card front">
    <div class="brand">
      <div class="brand__row">
        <span class="brand__mark"></span>
        <span class="brand__name">Ironbark Boring Group</span>
      </div>
      <div class="brand__region">Western Australia</div>
    </div>

    <div class="person">
      <div class="person__name">Gavin Thorley</div>
      <div class="person__role">Managing Director</div>
    </div>

    <div class="divider"></div>

    <div class="band">
      <div class="contacts">
        <div class="contacts__text">
          <div class="contacts__phone">0481639207</div>
          <div class="contacts__email">gavin@ibgpty.com.au</div>
          <div class="contacts__web">www.ibgpty.com.au</div>
        </div>
        <div class="contacts__rule"></div>
        <div class="contacts__icons">
          <svg viewBox="0 0 16 16" aria-label="Mobile"><g fill="#fff"><rect x="1" y="11" width="2.5" height="4"/><rect x="5" y="8" width="2.5" height="7"/><rect x="9" y="5" width="2.5" height="10"/><rect x="13" y="2" width="2.5" height="13"/></g></svg>
          <svg viewBox="0 0 16 16" aria-label="Email"><g fill="none" stroke="#fff" stroke-width="1.4"><rect x="1" y="3.5" width="14" height="9"/><path d="M1 3.5l7 5.5 7-5.5"/></g></svg>
          <svg viewBox="0 0 16 16" aria-label="Website"><g fill="none" stroke="#fff" stroke-width="1.3"><circle cx="8" cy="8" r="6.5"/><ellipse cx="8" cy="8" rx="3" ry="6.5"/><path d="M1.5 8h13M2.6 4.8h10.8M2.6 11.2h10.8"/></g></svg>
        </div>
      </div>
    </div>
  </section>

</main>
</body>
</html>
```